Eye-catching Yellow Page Ad for Attorney's Office

We need a phone book advertisement for our law office. We practice workers' compensation law, and our clientele consists exclusively of individuals who have been injured on the job. The dimensions of the print ad will be 6" W X 4.54" H.

We've had our current ad for several years, and wanted to get a new one that has been designed by a professional. Being that it's an ad for a law firm, it needs to be professional looking, but we're hoping to have something that looks a little more modern and has eye-catching appeal. We like the text that is included in the ad, and we want to make sure our phone number is very visible. No real preference for color scheme.

I've attached a copy of our current ad. All the information included in there is accurate. Our office name is Thornbury & Lisle, PLLC. The ethical rules for attorney advertising require the PLLC to be included in the ad, but it can be smaller than the other text (see our current ad).

Target Market(s)

Our potential clients are injured workers looking for legal representation in their workers' compensation claim.

Industry/Entity Type

Attorney

Font styles to use
Serif
Sans Serif

Requirements
Must have
• Professional, but stands out from the crowd
Nice to have
• Clean modern design
Should not have
• We don't want it to be too crowded or over-worked.

```html
<!DOCTYPE html>
<html lang="en">
<head>
<meta charset="utf-8">
<title>Thornbury &amp; Lisle, PLLC</title>
<link rel="stylesheet" href="https://fonts.googleapis.com/css2?family=Anton&family=Roboto+Condensed:wght@300;400;500;700&display=swap">
<style>
  :root {
    --gold: #d3b73f;
    --charcoal: #3a3b38;
    --ink: #2f3230;
    --panel: #e8ecea;
    --paper: #ffffff;
    --leather-light: #8a5532;
    --leather-dark: #3a2418;
    --pages: #e9e0cf;
  }
  * { margin: 0; padding: 0; box-sizing: border-box; }
  html, body { width: 1200px; height: 908px; overflow: hidden; background: var(--paper); }
  .ad {
    position: relative; width: 1200px; height: 908px; overflow: hidden;
    background: var(--paper);
    font-family: "Roboto Condensed", "Arial Narrow", sans-serif; color: var(--ink);
  }
  .top-rule { position: absolute; left: 0; top: 0; width: 100%; height: 9px; background: var(--charcoal); }
  .firm-name { position: absolute; left: 76px; top: 30px; width: 1024px; height: 180px; }
  .firm-name text { font-family: "Anton", "Impact", sans-serif; fill: var(--gold); }
  .entity-type {
    position: absolute; left: 1094px; top: 36px; font-weight: 700; font-size: 28px;
    color: var(--ink); letter-spacing: 0.5px;
  }
  .tagline { position: absolute; left: 80px; top: 232px; font-size: 37px; font-weight: 500; letter-spacing: 0.2px; }
  .intro { position: absolute; left: 80px; top: 281px; font-size: 28px; font-weight: 400; line-height: 41px; }
  .intro strong { font-weight: 700; }
  .services {
    position: absolute; left: 0; top: 398px; width: 960px; height: 260px; background: var(--panel);
  }
  .services h2 { position: absolute; left: 80px; top: 24px; font-size: 35px; font-weight: 300; }
  .service-list { list-style: none; position: absolute; font-size: 30px; font-weight: 500; line-height: 40px; }
  .service-list li { position: relative; padding-left: 26px; }
  .service-list li::before {
    content: ""; position: absolute; left: 0; top: 15px; width: 10px; height: 10px; background: var(--gold);
  }
  .service-list.col-a { left: 68px; top: 75px; }
  .service-list.col-b { left: 533px; top: 75px; }
  .website { position: absolute; left: 68px; top: 702px; font-size: 32px; font-weight: 500; }
  .contact-band { position: absolute; left: 0; top: 753px; width: 100%; height: 155px; background: var(--charcoal); }
  .phone { position: absolute; left: 60px; top: 6px; color: var(--gold); font-weight: 700; white-space: nowrap; }
  .phone .area { font-size: 50px; vertical-align: 4px; }
  .phone .number { font-size: 106px; letter-spacing: -1px; line-height: 1; }
  .address { position: absolute; left: 60px; top: 106px; color: var(--paper); font-size: 24px; }
  .gavel-art { position: absolute; left: 615px; top: 480px; width: 585px; height: 400px; }
  .partners {
    position: absolute; left: 700px; top: 722px; color: var(--gold); font-weight: 700;
    font-size: 28px; line-height: 40px; transform: rotate(-6deg); transform-origin: left top;
  }
</style>
</head>
<body>
<div class="ad">
  <div class="top-rule"></div>

  <svg class="firm-name" viewBox="0 0 1024 180" aria-label="Thornbury &amp; Lisle">
    <text x="0" y="155" font-size="152" textLength="1010" lengthAdjust="spacingAndGlyphs">Thornbury <tspan font-size="70">&amp;</tspan> Lisle</text>
  </svg>
  <div class="entity-type">PLLC</div>

  <h1 class="tagline">Former Assistant Attorneys General Who Know The System</h1>
  <p class="intro">At Thornbury &amp; Lisle, we provide <strong>personal</strong> attention to our clients.<br>That means your case is handled by an attorney, not an assistant.</p>

  <section class="services">
    <h2>We can help with:</h2>
    <ul class="service-list col-a">
      <li>Workplace injuries or death</li>
      <li>Lost wages</li>
      <li>Medical expenses &amp; treatment</li>
      <li>Hearing loss claims</li>
    </ul>
    <ul class="service-list col-b">
      <li>Pension claims</li>
      <li>Disability awards</li>
      <li>Return to work issues</li>
    </ul>
  </section>

  <p class="website">www.thornburylisle.com</p>

  <footer class="contact-band">
    <p class="phone"><span class="area">360</span><span class="number">555.0142</span></p>
    <p class="address">245 W. Harbor Suite 410, Fairhaven</p>
  </footer>

  <svg class="gavel-art" viewBox="0 0 585 400" role="img" aria-label="Photo of a wooden gavel resting on a thick leather-bound law book">
    <defs>
      <linearGradient id="photo-tone" x1="0" y1="0" x2="1" y2="0">
        <stop offset="0" stop-color="#3a2418"/>
        <stop offset="0.45" stop-color="#6b4127"/>
        <stop offset="1" stop-color="#e9e0cf"/>
      </linearGradient>
    </defs>
    <rect x="265" y="0" width="190" height="170" rx="18" fill="url(#photo-tone)"/>
    <rect x="0" y="150" width="585" height="250" rx="18" fill="url(#photo-tone)"/>
  </svg>
  <p class="partners">Miles Thornbury<br>Clara Lisle</p>
</div>
</body>
</html>
```